PV Hair and Beauty flyer

Hello I have hairdressing salon called PV Hair and Beauty.I need flyer with double side pls.On front side I need this picture to be there and under the pisture our full address,tel number and email address( 48 Fenwick rd E17 9QP 02074613398 media@pvhairandbeauty.co.uk). And under that shoud be written:Special offers
with 3 different discount squares at the bottom of the flyer.First visite 20% off,Second 15% off, thrd 10% off.At he other side of flyer should be following info:Ladies cut & blowdry with 3 different levels of stylist £45-£65,Gents cut £15-£36,Highlights from £45-£120,Express Blowdry £22-£35,Keratin tretmant £150,Manicure from £14,Pedicure from £25,Shellac from £28

```html
<!DOCTYPE html>
<html lang="en">
<head>
<meta charset="utf-8">
<title>PV Hair and Beauty – Price List</title>
<link href="https://fonts.googleapis.com/css2?family=Arvo:wght@400;700&display=swap" rel="stylesheet">
<style>
  :root {
    --bg-sand: #bfad88;
    --text-light: #ffffff;
    --brand-ink: #1e1e1e;
  }
  html, body {
    margin: 0;
    padding: 0;
    overflow: hidden;
    background: var(--bg-sand);
  }
  .flyer-back {
    position: relative;
    width: 1200px;
    height: 850px;
    background: var(--bg-sand);
    overflow: hidden;
    font-family: "Arvo", Georgia, serif;
  }
  .brand-name {
    position: absolute;
    top: 100px;
    left: 0;
    width: 100%;
    margin: 0;
    text-align: center;
    font-size: 17px;
    font-weight: 400;
    color: var(--brand-ink);
    letter-spacing: 0.02em;
  }
  .price-list {
    position: absolute;
    top: 178px;
    left: 57px;
    width: 1083px;
    margin: 0;
    padding: 0;
    list-style: none;
  }
  .price-item {
    display: flex;
    justify-content: space-between;
    align-items: baseline;
    height: 71.5px;
    line-height: 71.5px;
    color: var(--text-light);
  }
  .service-name {
    font-size: 33px;
    font-weight: 400;
    letter-spacing: 0.01em;
  }
  .service-price {
    font-size: 34px;
    font-weight: 700;
  }
</style>
</head>
<body>
  <main class="flyer-back">
    <p class="brand-name">PV Hair and Beauty</p>
    <ul class="price-list">
      <li class="price-item"><span class="service-name">Ladies cut &amp; blowdry with 3 different levels of stylist</span><span class="service-price">£45-£65</span></li>
      <li class="price-item"><span class="service-name">Gents cut</span><span class="service-price">£15-£36</span></li>
      <li class="price-item"><span class="service-name">Highlights</span><span class="service-price">£45-£120</span></li>
      <li class="price-item"><span class="service-name">Express Blowdry</span><span class="service-price">£22-£35</span></li>
      <li class="price-item"><span class="service-name">Keratin tretmant</span><span class="service-price">£150</span></li>
      <li class="price-item"><span class="service-name">Manicure</span><span class="service-price">£14</span></li>
      <li class="price-item"><span class="service-name">Pedicure</span><span class="service-price">£25</span></li>
      <li class="price-item"><span class="service-name">Shellac</span><span class="service-price">£28</span></li>
    </ul>
  </main>
</body>
</html>
```